Business Card Design

we are a brand new cable TV network devoted to self improvement and leading a better life called FLOURIVO TV.I have a logo. We have 3 executives that need cards.I want it to be a heavy stock card: professional but showing our creative nature

Industry/Entity Type

Business

Contact Information for Business Card

CLAUDIA SAENZ AMLIECEO350 San Juan DrPonte Vedra Beach FL 32082904-473-5953

```html
<!DOCTYPE html>
<html lang="en">
<head>
<meta charset="utf-8">
<title>FLOURIVO TV Business Card</title>
<link rel="stylesheet" href="https://fonts.googleapis.com/css2?family=Jost:wght@400;500;700&display=swap">
<style>
  :root {
    --backdrop: #e9e6e2;
    --card-black: #000000;
    --card-white: #ffffff;
    --brand-red: #c0232b;
    --brand-red-light: #e0645f;
    --ink: #1f1f1f;
    --ink-soft: #3a3a3a;
    --rule: #555555;
  }
  * { box-sizing: border-box; margin: 0; padding: 0; }
  html, body {
    width: 1200px;
    height: 1000px;
    overflow: hidden;
    background: var(--backdrop);
    font-family: "Jost", sans-serif;
  }
  .canvas { position: relative; width: 1200px; height: 1000px; }

  .card {
    position: absolute;
    left: 265px;
    width: 665px;
    height: 397px;
    border-radius: 24px;
    box-shadow: 0 6px 16px rgba(0,0,0,0.18);
    overflow: hidden;
  }
  .card--front { top: 73px; background: var(--card-black); }
  .card--back { top: 533px; background: var(--card-white); }

  .brand-name {
    position: absolute;
    font-family: "Jost", sans-serif;
    font-weight: 700;
    white-space: nowrap;
    letter-spacing: 1px;
  }
  .card--front .brand-name {
    left: 0; right: 0;
    top: 165px;
    text-align: center;
    font-size: 66px;
    line-height: 1;
    color: var(--card-white);
  }
  .card--back .brand-name {
    left: 33px;
    top: 56px;
    font-size: 46px;
    line-height: 1;
    color: var(--ink);
  }

  .holder-name {
    position: absolute;
    left: 33px;
    top: 195px;
    font-size: 22px;
    font-weight: 700;
    color: var(--brand-red);
  }
  .holder-title {
    position: absolute;
    left: 33px;
    top: 226px;
    display: flex;
    align-items: center;
    gap: 6px;
    font-size: 17px;
    font-weight: 400;
    color: var(--ink-soft);
  }
  .holder-title .rule {
    width: 185px;
    height: 2px;
    background: linear-gradient(to right, var(--rule), rgba(85,85,85,0.1));
  }

  .contact {
    position: absolute;
    left: 33px;
    display: flex;
    align-items: flex-start;
    gap: 5px;
    font-size: 18px;
    line-height: 25px;
    color: var(--ink);
  }
  .contact svg { flex: none; margin-top: 4px; }
  .contact--phone { top: 285px; }
  .contact--address { top: 319px; }

  .brand-disc {
    position: absolute;
    left: 380px;
    top: 135px;
    width: 230px;
    height: 230px;
    border-radius: 50%;
    background: linear-gradient(to bottom, var(--brand-red-light), var(--brand-red));
  }
</style>
</head>
<body>
<main class="canvas">
  <section class="card card--front" aria-label="Card front">
    <div class="brand-name">FLOURIVO TV</div>
  </section>

  <section class="card card--back" aria-label="Card back">
    <div class="brand-name">FLOURIVO TV</div>

    <div class="holder-name">Mirella Okafor Dunst</div>
    <div class="holder-title"><span>CEO</span><span class="rule"></span></div>

    <div class="contact contact--phone">
      <svg width="18" height="18" viewBox="0 0 24 24" aria-hidden="true">
        <path fill="#c0232b" d="M6.6 10.8a15.1 15.1 0 0 0 6.6 6.6l2.2-2.2a1 1 0 0 1 1-.25 11.4 11.4 0 0 0 3.6.57 1 1 0 0 1 1 1V20a1 1 0 0 1-1 1A17 17 0 0 1 3 4a1 1 0 0 1 1-1h3.5a1 1 0 0 1 1 1c0 1.25.2 2.45.57 3.57a1 1 0 0 1-.25 1z"/>
        <path fill="none" stroke="#c0232b" stroke-width="2" stroke-linecap="round" d="M14 3a7 7 0 0 1 7 7M14 7a3 3 0 0 1 3 3"/>
      </svg>
      <span>904-618-2047</span>
    </div>

    <div class="contact contact--address">
      <svg width="16" height="20" viewBox="0 0 16 22" aria-hidden="true">
        <path fill="#c0232b" d="M8 0a8 8 0 0 0-8 8c0 6 8 14 8 14s8-8 8-14a8 8 0 0 0-8-8zm0 11a3 3 0 1 1 0-6 3 3 0 0 1 0 6z"/>
      </svg>
      <span>718 Harlow Creek Dr<br>Ponte Vedra Beach FL 32097</span>
    </div>

    <div class="brand-disc" aria-hidden="true"></div>
  </section>
</main>
</body>
</html>
```